Design Business Card MAPLE WREN MOWING

We have attached a copy of our Logo, we like a business card designed with logo and mobile phone number on one side that stands out maybe gloss and on the other side it can have the services we do small picture of our logo name number, I have attached an idea to this that I have seen online, this is a business owned by a woman so we like pinks black and navy
Our logo is attached in pdf
Target Market(s)
Home owners that need lawns mowed
Industry/Entity Type
Lawns and gardens
Contact Information for Business Card
Logo business Owner name Deborah Finch mobile number 0491627504
Font styles to use
Look and feel
Each slider illustrates characteristics of the customer's brand and the style your logo design should communicate.

```html
<!DOCTYPE html>
<html lang="en">
<head>
<meta charset="utf-8">
<title>Maple Wren Mowing – Business Card</title>
<link rel="stylesheet" href="https://fonts.googleapis.com/css2?family=Saira+Condensed:wght@700;800&family=Saira+Semi+Condensed:wght@600;700&family=Rajdhani:wght@600&display=swap">
<style>
  :root {
    --page: #ece7df;
    --black: #050505;
    --pink: #e55aa8;
    --pink-deep: #c63f8b;
    --green: #3bb54a;
    --yellow: #f0c160;
    --gold: #e9c45e;
    --gold-deep: #c99a32;
  }
  html, body {
    margin: 0;
    width: 900px;
    height: 1200px;
    overflow: hidden;
    background: var(--page);
  }
  .canvas {
    position: relative;
    width: 900px;
    height: 1200px;
  }
  .card {
    position: absolute;
    left: 80px;
    width: 738px;
    height: 427px;
    border-radius: 22px;
    overflow: hidden;
    box-shadow: 0 8px 18px rgba(0,0,0,0.35);
  }
  .card--front { top: 125px; }
  .card--back  { top: 638px; }
  .card__bg {
    position: absolute;
    inset: 0;
    width: 100%;
    height: 100%;
  }
  .brand-name {
    position: absolute;
    margin: 0;
    font-family: "Saira Condensed", sans-serif;
    font-weight: 800;
    color: var(--black);
    text-align: center;
    line-height: 0.95;
    letter-spacing: 1px;
  }
  .card--front .brand-name {
    left: 0; right: 0;
    top: 180px;
    font-size: 64px;
  }
  .card--back .brand-name {
    left: 0; right: 0;
    top: 50px;
    font-size: 92px;
  }
  .brand-mark {
    display: inline-block;
    width: 0.32em;
    height: 0.32em;
    border-radius: 50%;
    background: var(--black);
    vertical-align: middle;
    margin-right: 0.2em;
  }
  .phone-line {
    position: absolute;
    left: 0; right: 0;
    top: 352px;
    display: flex;
    justify-content: center;
    align-items: center;
    gap: 12px;
    font-family: "Saira Condensed", sans-serif;
    font-weight: 700;
    font-size: 38px;
    letter-spacing: 2px;
    color: var(--gold);
  }
  .phone-icon { width: 42px; height: 42px; }
  .services {
    position: absolute;
    left: 0; right: 0;
    top: 266px;
    margin: 0;
    font-family: "Saira Semi Condensed", sans-serif;
    font-weight: 700;
    font-size: 20px;
    letter-spacing: 0.6px;
    line-height: 32px;
    color: var(--gold);
    text-align: center;
  }
  .services .sep {
    color: var(--gold-deep);
    font-size: 14px;
    margin: 0 6px;
    vertical-align: 2px;
  }
  .contact {
    position: absolute;
    left: 275px;
    width: 190px;
    top: 350px;
    text-align: center;
    color: var(--black);
  }
  .contact__phone {
    font-family: "Saira Condensed", sans-serif;
    font-weight: 700;
    font-size: 33px;
    letter-spacing: 2px;
    line-height: 1;
  }
  .contact__email {
    font-family: "Rajdhani", sans-serif;
    font-weight: 600;
    font-size: 15px;
    margin-top: 6px;
  }
</style>
</head>
<body>
<main class="canvas">

  <section class="card card--front" aria-label="Business card front">
    <svg class="card__bg" viewBox="0 0 738 427" preserveAspectRatio="none">
      <defs>
        <linearGradient id="front-top" x1="0" y1="0" x2="0" y2="1">
          <stop offset="0" stop-color="#f0c160"/>
          <stop offset="0.6" stop-color="#3bb54a"/>
        </linearGradient>
        <linearGradient id="front-bottom" x1="0" y1="0" x2="1" y2="0">
          <stop offset="0.55" stop-color="#3bb54a"/>
          <stop offset="1" stop-color="#f0c160"/>
        </linearGradient>
        <linearGradient id="front-grass" x1="0" y1="0" x2="0" y2="1">
          <stop offset="0" stop-color="#d96aae"/>
          <stop offset="1" stop-color="#c9529a"/>
        </linearGradient>
      </defs>
      <rect width="738" height="427" fill="var(--black)"/>
      <rect width="738" height="130" fill="url(#front-top)"/>
      <path d="M0 72 Q369 150 738 72 L738 427 L0 427 Z" fill="var(--black)"/>
      <path d="M0 300 Q369 270 738 292 L738 427 L0 427 Z" fill="url(#front-bottom)"/>
      <path d="M0 330 Q369 290 738 340 L738 427 L0 427 Z" fill="var(--black)"/>
      <path d="M0 92 Q369 165 738 92 L738 318 Q369 290 0 318 Z" fill="url(#front-grass)" role="img" aria-label="Pink grass texture band"/>
      <rect x="190" y="45" width="360" height="290" rx="145" fill="var(--pink-deep)" opacity="0.35" role="img" aria-label="Logo illustration area: lawn mower with grass"/>
    </svg>
    <h1 class="brand-name"><span class="brand-mark"></span>MAPLE WREN<br>MOWING</h1>
    <div class="phone-line">
      <svg class="phone-icon" viewBox="0 0 42 42" aria-hidden="true">
        <circle cx="21" cy="21" r="18" fill="none" stroke="var(--gold)" stroke-width="3"/>
        <path d="M14 12 l4 -1 l3 6 l-3 2 q2 5 6 7 l2 -3 l6 3 l-1 4 q-2 2 -6 1 q-9 -4 -12 -13 q-1 -4 1 -6 Z" fill="var(--gold)"/>
      </svg>
      <span>000 000 000</span>
    </div>
  </section>

  <section class="card card--back" aria-label="Business card back">
    <svg class="card__bg" viewBox="0 0 738 427" preserveAspectRatio="none">
      <defs>
        <linearGradient id="back-bottom" x1="0" y1="0" x2="1" y2="0">
          <stop offset="0.35" stop-color="#3bb54a"/>
          <stop offset="1" stop-color="#f0c160"/>
        </linearGradient>
      </defs>
      <rect width="738" height="427" fill="var(--pink)"/>
      <path d="M0 200 Q369 300 738 200 L738 427 L0 427 Z" fill="var(--black)"/>
      <path d="M0 350 Q369 320 738 345 L738 427 L0 427 Z" fill="url(#back-bottom)"/>
    </svg>
    <h2 class="brand-name"><span class="brand-mark"></span>MAPLE WREN<br>MOWING</h2>
    <p class="services">
      GARDEN MAINTENANCE<span class="sep">▼</span>RUBBISH REMOVAL<span class="sep">▼</span>TRIMMING<br>
      WEEDING<span class="sep">▼</span>LAWN CARE
    </p>
    <div class="contact">
      <div class="contact__phone">000 000 000</div>
      <div class="contact__email">info@maplewren.com</div>
    </div>
  </section>

</main>
</body>
</html>
```